Website Wordpress Responsive Design and Development - Landscape Company

Site is currently under construction, but the old site needs a refresh.
Need a fully responsive wordpress website (built in Elementor or comparable theme).
Here's the way it looked prior :
https://pastpages.example/snap/20220330041341/http://brookmoorgreens.example/
Their current designer came up with a website sample and it looks terrible :
https://talkowenpics.sitebuild.example/mysite/projects
Websites the client likes for some inspiration, but needs better than these :
https://www.quarrinbeckgroundworkers.example/
http://kvatelierpx.example/
https://tullidgepartners.example/
https://www.garbettcoinc.example/

Navigation includes :
• Home
• Complete structure of website content is available in the home page, yielding main information on services.
• Visually appealing but simple to use and navigate. Subtle amount of content, but enough for search engines to be able to read up the target phrases.
• Sections on the home page include :
▪ About - Information about the company and main service focus
▪ Gallery - Imagery categorized to include lightbox style zoom.
▪ Contact - Contact details and connection information
• About
• Bannered header
• Content appropriately formatted to subject
• Gallery
• Bannered header
• Each of the albums would have their own categorized image content
• Contact
• Bannered header
• Social Media connector available on all pages (like box, feed, etc) if applicable
• Content can be updated on all pages
• Basic Optimization for SEO with title tags, meta data where applicable.
• Google Analytics and Sitemap installed. (google account will be provided)
• Google Business Listing and Search Console Accounts created

Coded - Design and coding required

1 page

• Wordpress Responsive Design

```html
<!DOCTYPE html>
<html lang="en">
<head>
<meta charset="utf-8">
<title>Brookmoor Greens — Landscape Construction and Maintenance</title>
<link rel="stylesheet" href="https://fonts.googleapis.com/css2?family=Saira+Semi+Condensed:wght@600;700&family=Roboto:wght@400;500;700&display=swap">
<style>
:root{
  --green:#2a9a1c;
  --green-dark:#1d7a12;
  --ink:#111;
  --text:#666;
  --cream:#f3f2ea;
  --line:#d9d9d9;
  --white:#fff;
}
*{box-sizing:border-box;margin:0;padding:0}
html,body{width:1200px;height:3974px;overflow:hidden;background:var(--white)}
body{font-family:"Roboto",sans-serif;color:var(--text);position:relative}
h1,h2,h3,h4,.brand{font-family:"Saira Semi Condensed",sans-serif;color:var(--ink);font-weight:700}
a{color:inherit;text-decoration:none}
.abs{position:absolute}
.label{font-size:14px;font-weight:500;color:var(--green-dark);letter-spacing:.2px;text-transform:uppercase}
.btn{display:inline-flex;align-items:center;justify-content:center;background:var(--green);color:var(--white);border-radius:30px;font-weight:700;font-size:14px}

/* header */
.brand-block{left:0;top:0;width:350px;height:163px;background:#000}
.brand{left:86px;top:28px;font-size:27px;color:var(--white);font-weight:700}
.contact-top{top:22px;display:flex;align-items:center;gap:14px}
.contact-top .ico{width:56px;height:56px;border-radius:50%;background:#e6f2e2;display:flex;align-items:center;justify-content:center}
.contact-top b{display:block;font-size:17px;color:var(--ink)}
.contact-top small{font-size:12px;color:#888}
.sep{left:609px;top:26px;width:1px;height:46px;background:var(--line)}
.quote-btn{left:963px;top:20px;width:150px;height:58px;font-size:15px}
.nav{left:85px;top:102px;width:851px;height:61px;background:var(--white);display:flex;align-items:center;padding-left:30px;gap:20px;font-size:15px;font-weight:700;color:var(--green-dark)}
.nav .dot{width:7px;height:7px;background:var(--green);transform:rotate(45deg)}
.nav .active{color:var(--green)}
.nav-black{left:936px;top:102px;width:264px;height:61px;background:#000}
.social-top{left:936px;top:102px;display:flex}
.social-top span{width:59px;height:61px;border-left:1px solid #333;display:flex;align-items:center;justify-content:center}
.social-top i{width:14px;height:14px;border-radius:50%;border:2px solid var(--white)}

/* hero */
.hero{left:0;top:163px;width:1200px;height:651px;background:linear-gradient(180deg,#8c9196 0%,#b8b4ad 32%,#9a9186 55%,#5c8a2e 72%,#4fa81d 100%)}
.hero-title{left:85px;top:339px;width:600px;font-size:50px;line-height:59px;color:var(--white)}
.hero-title span{background:#000;padding:0 6px 0 7px;box-decoration-break:clone;-webkit-box-decoration-break:clone}

/* about */
.about-label{left:86px;top:917px}
.about h2{left:86px;top:950px;width:520px;font-size:33px;line-height:40px}
.about p{left:86px;width:480px;font-size:14px;line-height:22px}
.about .btn{left:85px;top:1321px;width:150px;height:58px}
.ph{background:linear-gradient(180deg,#c9ccd0 0%,#a5533c 30%,#8d4434 55%,#3f8a22 75%,#2f7a18 100%)}
.badge{left:790px;top:1074px;width:144px;height:144px;border-radius:50%;background:var(--green);color:var(--white);text-align:center;font-weight:700;font-size:15px;line-height:19px;padding-top:44px}

/* services */
.services{left:0;top:1484px;width:1200px;height:635px;background:var(--cream)}
.center{left:0;width:1200px;text-align:center}
.svc-title{font-size:33px;line-height:40px}
.card{top:1716px;width:326px;height:253px;background:var(--white);padding:6px}
.card .in{border:2px solid var(--green);height:100%;text-align:center;padding-top:22px}
.card h3{font-size:23px;margin:14px 0 14px}
.card p{font-size:14px;line-height:22px;padding:0 30px}
.view{font-size:14px;color:var(--ink)}
.view u{font-weight:700}

/* gallery */
.gal{background:linear-gradient(180deg,#9aa0a4 0%,#b3ada0 35%,#8f8270 55%,#4d8f25 75%,#3d7d1d 100%)}
.gal.alt{background:#3f7d2c}
.plus{left:326px;top:2474px;width:74px;height:74px;border-radius:50%;background:var(--white);display:flex;align-items:center;justify-content:center}

/* quote */
.quote{left:0;top:2799px;width:1200px;height:686px;background:radial-gradient(ellipse at 30% 40%,#e9ebe2 0%,#cfd6c4 45%,#a8b59a 80%,#8f9e80 100%)}
.quote h2{font-size:33px}
.field{height:58px;background:var(--white);border-radius:29px;font-size:14px;color:#999;padding:20px 27px}
.reach h2{font-size:33px;line-height:40px}
.ci{left:737px;display:flex;gap:18px;align-items:center}
.ci b{display:block;font-size:18px;color:var(--green-dark)}
.ci small{font-size:12px;color:#888}

/* footer */
.foot h4{font-size:19px;text-decoration:underline;color:var(--green-dark);top:3585px}
.foot p{font-size:14px;line-height:22px}
.links{list-style:none;font-size:14px;line-height:39.5px}
.links li::before{content:"›";color:var(--ink);font-size:22px;margin-right:16px}
.info{font-size:14px;line-height:22px}
.info b{color:#444}
.copy-line{top:3915px;height:1px;background:var(--line)}
</style>
</head>
<body>

<header>
  <div class="abs brand-block"></div>
  <div class="abs brand">Brookmoor Greens</div>

  <div class="abs contact-top" style="left:378px">
    <span class="ico"><svg width="30" height="30" viewBox="0 0 24 24" fill="none" stroke="#2a9a1c" stroke-width="1.4"><path d="M5 3l4 1 1 5-2 1a12 12 0 0 0 6 6l1-2 5 1 1 4-3 2C10 20 4 14 3 6z"/></svg></span>
    <span><b>(555) 014-2270</b><small>PHONE</small></span>
  </div>
  <div class="abs sep"></div>
  <div class="abs contact-top" style="left:630px">
    <span class="ico"><svg width="32" height="28" viewBox="0 0 26 22" fill="none" stroke="#2a9a1c" stroke-width="1.4"><rect x="1" y="4" width="24" height="17"/><path d="M1 4l12 9 12-9M1 21l9-8M25 21l-9-8"/></svg></span>
    <span><b>dale@brookmoorgreens.example</b><small>EMAIL</small></span>
  </div>
  <a class="abs btn quote-btn">Get A Quote&nbsp;&nbsp;<svg width="16" height="16" viewBox="0 0 16 16" fill="none" stroke="#fff" stroke-width="1.4"><path d="M9 2H2v12h7M6 8h9M12 5l3 3-3 3"/></svg></a>

  <nav class="abs nav">
    <a class="active">Home</a><i class="dot"></i><a>About</a><i class="dot"></i><a>Services</a><i class="dot"></i><a>Gallery</a><i class="dot"></i><a>Contact</a>
  </nav>
  <div class="abs nav-black"></div>
  <div class="abs social-top" aria-label="Social links"><span><i></i></span><span><i></i></span><span><i></i></span></div>
</header>

<section>
  <div class="abs hero" role="img" aria-label="Photo of a large shingled estate home behind tall green lawn grass at dusk"></div>
  <h1 class="abs hero-title"><span>landscape construction and maintenance company</span></h1>
</section>

<section class="about">
  <div class="abs label about-label">About Us</div>
  <h2 class="abs">A full service landscape construction and maintenance company</h2>
  <p class="abs" style="top:1089px">We have been servicing the community for over 20 years and in that time have established ourselves as a premier contractor in the Hamptons. We pride ourselves on quality work and excellent customer service.</p>
  <p class="abs" style="top:1166px">At an early age, Dale Harwick began mowing lawns for local families. As he got older, the number of lawn accounts began to grow. In 1998, Dale Harwick incorporated his small maintenance company taking it to the next level.Today, Brookmoor Greens services over 200 residential, municipal, and commercial properties and works with several local builders.</p>
  <a class="abs btn">More About Us</a>
  <div class="abs ph" style="left:613px;top:919px;width:238px;height:461px" role="img" aria-label="Photo of a red brick carriage house with white trim and a green lawn"></div>
  <div class="abs ph" style="left:876px;top:919px;width:238px;height:461px" role="img" aria-label="Photo of a brick building with arched white garage doors and a stone drive"></div>
  <div class="abs badge"><svg width="36" height="26" viewBox="0 0 36 26" fill="none" stroke="#fff" stroke-width="1.4" style="display:block;margin:-30px auto 8px"><path d="M4 24h28M10 24v-8l8-6 8 6v8M18 4v6"/></svg>20 Years<br>of Experience</div>
</section>

<section>
  <div class="abs services"></div>
  <div class="abs center label" style="top:1586px">Our Services</div>
  <h2 class="abs center svc-title" style="top:1608px">The Best Choice For Your<br>Business.</h2>

  <div class="abs card" style="left:85px"><div class="in">
    <svg width="66" height="60" viewBox="0 0 66 60" fill="none" stroke="#2a9a1c" stroke-width="2"><path d="M6 52c14-8 40-8 54 0M18 46c6-4 24-4 30 0M33 44V20M33 30c-6-2-8-8-6-12 6 2 8 8 6 12zM33 26c6-2 9-7 7-11-6 2-8 7-7 11z"/><circle cx="48" cy="10" r="5"/></svg>
    <h3>Landscaping</h3><p>Dale Harwick, President, personally oversees all projects along with Owen Pryce...</p></div></div>
  <div class="abs card" style="left:436px"><div class="in">
    <svg width="66" height="60" viewBox="0 0 66 60" fill="none" stroke="#2a9a1c" stroke-width="2"><path d="M20 54V30M20 30c-10 0-12-14-6-22 4 6 10 4 12 12 2 8-2 10-6 10zM36 8l6 36M42 44l12 6M42 44l-8 8"/></svg>
    <h3>Maintenance</h3><p>Brookmoor Greens maintenance crews pride themselves on professionalism and experience.</p></div></div>
  <div class="abs card" style="left:787px"><div class="in">
    <svg width="66" height="60" viewBox="0 0 66 60" fill="none" stroke="#2a9a1c" stroke-width="2"><rect x="8" y="26" width="46" height="28" rx="3"/><path d="M20 26V10M20 14c-6-2-6-8-2-10 4 2 4 8 2 10zM34 26V8M34 12c6-2 6-8 2-10-4 2-4 8-2 10zM46 26V14"/></svg>
    <h3>Flowers</h3><p>Brookmoor Greens can design, install, and maintain your annual container plantings.</p></div></div>

  <div class="abs center view" style="top:2000px">View <u>All Services</u></div>
</section>

<section>
  <div class="abs center label" style="top:2221px">Our Gallery</div>
  <h2 class="abs center" style="top:2254px;font-size:33px">Worked We Have Done</h2>
  <div class="abs gal" style="left:14px;top:2327px;width:224px;height:367px" role="img" aria-label="Photo of a shingle-style estate with a cobblestone motor court"></div>
  <div class="abs gal alt" style="left:251px;top:2347px;width:224px;height:325px" role="img" aria-label="Photo of a stepping-stone path through a shaded garden"></div>
  <div class="abs plus"><svg width="34" height="34" viewBox="0 0 34 34" stroke="#2a9a1c" stroke-width="2"><path d="M17 2v30M2 17h30"/></svg></div>
  <div class="abs gal" style="left:488px;top:2327px;width:224px;height:367px" role="img" aria-label="Photo of a house with a lawn bordered by a stone retaining wall"></div>
  <div class="abs gal" style="left:725px;top:2347px;width:224px;height:325px" role="img" aria-label="Photo of a shingled home with a broad front lawn"></div>
  <div class="abs gal" style="left:962px;top:2327px;width:224px;height:367px" role="img" aria-label="Photo of a curving asphalt driveway leading to a country house"></div>
</section>

<section>
  <div class="abs quote" role="img" aria-label="Soft blurred garden photo background"></div>
  <h2 class="abs" style="left:85px;top:2892px">Get a Free Quote Today.</h2>
  <div class="abs field" style="left:87px;top:2961px;width:277px">First name</div>
  <div class="abs field" style="left:376px;top:2961px;width:278px">Last name</div>
  <div class="abs field" style="left:87px;top:3038px;width:277px">Email</div>
  <div class="abs field" style="left:376px;top:3038px;width:278px">Phone</div>
  <div class="abs field" style="left:87px;top:3115px;width:567px">Address</div>
  <div class="abs field" style="left:87px;top:3192px;width:570px;height:110px;border-radius:36px">Type your message here</div>
  <a class="abs btn" style="left:85px;top:3325px;width:150px;height:58px">Submit</a>

  <div class="abs reach">
    <div class="abs label" style="left:737px;top:2900px;width:200px">Reach Out</div>
    <h2 class="abs" style="left:737px;top:2928px;width:420px">Top quality work and excellent customer service.</h2>
  </div>
  <div class="abs ci" style="top:3078px"><svg width="44" height="40" viewBox="0 0 24 24" fill="none" stroke="#2a9a1c" stroke-width="1.2"><path d="M5 3l4 1 1 5-2 1a12 12 0 0 0 6 6l1-2 5 1 1 4-3 2C10 20 4 14 3 6z"/></svg><span><b>(555) 014-2270</b><small>PHONE</small></span></div>
  <div class="abs ci" style="top:3156px"><svg width="44" height="38" viewBox="0 0 26 22" fill="none" stroke="#2a9a1c" stroke-width="1.2"><rect x="1" y="4" width="24" height="17"/><path d="M1 4l12 9 12-9"/></svg><span><b>dale@brookmoorgreens.example</b><small>EMAIL</small></span></div>
  <div class="abs ci" style="top:3242px"><svg width="44" height="38" viewBox="0 0 26 22" fill="none" stroke="#2a9a1c" stroke-width="1.2"><rect x="1" y="8" width="24" height="10" rx="2"/><path d="M6 8V2h14v6M6 15v6h14v-6"/></svg><span><b>(555) 014-2291</b><small>FAX</small></span></div>
</section>

<footer class="foot">
  <h4 class="abs" style="left:85px">About Us</h4>
  <p class="abs" style="left:85px;top:3640px;width:290px">At an early age, Dale Harwick began mowing lawns for local families. As he got older, the number of lawn accounts began to grow. In 1998, Dale Harwick incorporated his small maintenance company taking it to the next level.</p>
  <div class="abs" style="left:85px;top:3800px;display:flex;gap:24px" aria-label="Social links">
    <i style="width:16px;height:16px;border-radius:50%;background:var(--green-dark)"></i><i style="width:16px;height:16px;border-radius:50%;background:var(--green-dark)"></i><i style="width:16px;height:16px;border-radius:50%;background:var(--green-dark)"></i>
  </div>

  <h4 class="abs" style="left:472px">Quick Links</h4>
  <ul class="abs links" style="left:472px;top:3630px"><li>Home</li><li>About</li><li>Services</li><li>Gallery</li><li>Contact</li></ul>

  <h4 class="abs" style="left:678px">Solutions</h4>
  <ul class="abs links" style="left:678px;top:3630px"><li>Leadeership</li><li>Terms</li><li>Privacy Policy</li><li>Licenses</li><li>Sitemap</li></ul>

  <h4 class="abs" style="left:875px">Contact Info</h4>
  <div class="abs info" style="left:875px;top:3640px;width:250px">
    <p><b>Address:</b> PO Box 318 Westhaven, NY 10999</p>
    <p style="margin-top:18px"><b>Email:</b> Dale@BrookmoorGreens.example</p>
    <p style="margin-top:18px"><b>Phone:</b> (555) 014-2270</p>
    <p style="margin-top:18px"><b>Fax:</b> (555) 014-2291</p>
  </div>

  <div class="abs copy-line" style="left:85px;width:350px"></div>
  <div class="abs copy-line" style="left:765px;width:350px"></div>
  <div class="abs center" style="top:3904px;font-size:14px;color:#333">© 2020 Brookmoor Greens All rights reserved.</div>
</footer>

</body>
</html>
```